Banner Pop Up Opt In Form REDESIGNS - SLEEK BLACK LOOK

Please redesign banners attached.

I am looking for a very sleek look....I do not like this collage of images on these current designs. Please keep all content same but use images that pop.

I have an acccount at www.pixmorrow-example.com or you can use your own images.

I like black background for somereason because it looks very sleek....but these designs should pop , build trust and credibility and have easy opt in form....SLEEK AND MODERN LOOK is what im looking for....

Target Market(s)

Consumers on websites

Requirements
Must have
• Please redesign banners attached.

Nice to have

Should not have

```html
<!DOCTYPE html>
<html lang="en">
<head>
<meta charset="utf-8">
<title>Newsletter Offer Pop-Up</title>
<link rel="stylesheet" href="https://fonts.googleapis.com/css2?family=Montserrat:wght@500&family=Roboto:wght@300;400&display=swap">
<style>
  :root {
    --page-bg: #f7f7f7;
    --panel-bg: #0c0c0c;
    --panel-bg-edge: #1c1c1c;
    --accent-green: #34c796;
    --accent-red: #ff0a0a;
    --text-white: #ffffff;
    --text-muted: #cfcfcf;
    --field-border: #8a8a8a;
    --close-bg: #e9e9e9;
  }
  * { box-sizing: border-box; margin: 0; padding: 0; }
  html, body {
    width: 1200px; height: 1000px; overflow: hidden;
    background: var(--page-bg);
    font-family: "Roboto", Arial, sans-serif;
  }
  .popup {
    position: absolute; left: 133px; top: 38px; width: 911px; height: 910px;
    background: radial-gradient(circle at 70% 40%, var(--panel-bg-edge), var(--panel-bg) 70%);
    box-shadow: 0 10px 30px rgba(0,0,0,0.25);
    overflow: hidden;
  }
  .popup__photos { position: absolute; left: 0; top: 0; }
  .close-button {
    position: absolute; left: 1002px; top: 13px; width: 70px; height: 70px;
    border-radius: 50%; background: var(--close-bg);
    border: 2px solid #ffffff; box-shadow: 0 2px 6px rgba(0,0,0,0.35);
    font-family: "Roboto", Arial, sans-serif; font-weight: 300; font-size: 44px;
    line-height: 66px; text-align: center; color: #111;
  }
  .headline {
    position: absolute; right: 70px; top: 52px;
    font-family: "Montserrat", Arial, sans-serif; font-weight: 500;
    font-size: 54px; line-height: 56px; letter-spacing: 1px;
    color: var(--accent-green); text-align: right;
  }
  .subscribe-pill {
    position: absolute; left: 611px; top: 275px; width: 228px; height: 56px;
    border-radius: 28px; background: var(--accent-red);
    color: var(--text-white); font-weight: 300; font-size: 29px;
    line-height: 56px; text-align: center;
  }
  .cursor { position: absolute; left: 810px; top: 310px; }
  .lead {
    position: absolute; right: 82px; top: 346px;
    color: var(--text-white); font-weight: 300; font-size: 25px;
    line-height: 34px; text-align: right; letter-spacing: 0.3px;
  }
  .signup-form { position: absolute; left: 338px; top: 467px; width: 502px; }
  .field {
    height: 53px; margin-bottom: 16px; border: 2px solid var(--field-border);
    border-radius: 8px; padding-left: 15px;
    font-weight: 300; font-size: 21px; line-height: 49px; color: #9a9a9a;
  }
  .field--filled { border-color: var(--accent-green); color: var(--accent-green); }
  .submit-button {
    height: 54px; border-radius: 8px; background: var(--accent-green);
    color: var(--text-white); font-size: 21px; line-height: 54px; text-align: center;
  }
  .footnote {
    position: absolute; left: 160px; top: 798px; width: 751px; height: 82px;
    background: linear-gradient(90deg, rgba(20,20,20,0.9), #232323 80%, #2e2e2e);
    color: var(--text-muted); font-weight: 300; font-size: 21px;
    line-height: 27px; text-align: center; padding-top: 14px; padding-right: 160px;
  }
</style>
</head>
<body>
  <div class="popup">
    <svg class="popup__photos" width="911" height="910" viewBox="0 0 911 910">
      <defs>
        <linearGradient id="dining-tones" x1="0" y1="0" x2="1" y2="1">
          <stop offset="0" stop-color="#8a6a52"/>
          <stop offset="0.5" stop-color="#c9a27a"/>
          <stop offset="1" stop-color="#5a3a26"/>
        </linearGradient>
        <linearGradient id="grill-tones" x1="0" y1="0" x2="1" y2="1">
          <stop offset="0" stop-color="#d9d4cc"/>
          <stop offset="0.45" stop-color="#e89a2c"/>
          <stop offset="1" stop-color="#5c3320"/>
        </linearGradient>
      </defs>
      <g role="img" aria-label="Friends sharing plates of food and drinks around a restaurant table">
        <rect x="82" y="82" width="330" height="330" rx="26" transform="rotate(45 247 247)"
              fill="url(#dining-tones)" stroke="#ffffff" stroke-width="5"/>
      </g>
      <g role="img" aria-label="Close-up of grilled skewers with peppers and fresh rosemary">
        <rect x="-180" y="436" width="370" height="370" rx="26" transform="rotate(45 5 621)"
              fill="url(#grill-tones)" stroke="#ffffff" stroke-width="5"/>
      </g>
    </svg>

    <h1 class="headline">WANT<br>A GREAT<br>OFFER?</h1>

    <div class="subscribe-pill">SUBSCRIBE</div>
    <svg class="cursor" width="24" height="34" viewBox="0 0 24 34" aria-hidden="true">
      <path d="M2 2 L2 26 L8 20 L12 30 L16 28 L12 19 L20 19 Z" fill="#ffffff" stroke="#222" stroke-width="1.5" stroke-linejoin="round"/>
    </svg>

    <p class="lead">TO OUR&nbsp; NEWSLETTER<br>&amp; RECEIVE A&nbsp; COMPLIMENTARY</p>

    <div class="signup-form">
      <div class="field field--filled">John Smith</div>
      <div class="field">EMAIL</div>
      <div class="field">PHONE</div>
      <div class="submit-button">SUBMIT</div>
    </div>

    <p class="footnote">We will send an email and a text message<br>with the offer and instruction on how to redeem.</p>
  </div>

  <div class="close-button" aria-label="Close">X</div>
</body>
</html>
```